Modern card design needed for building development company

We are looking for a sharp modern new look for our business cards.
We are a New Zealand based company called TKV Ventures NZ LTD that specialises in subdividing large sections, housing and commercial buildings.
We have attached a photo of the current logo and would like to see it improved somehow as it looks a bit dated.
We are open to any colours.

Target Market(s)

Investors, Property buyers

Industry/Entity Type

Investment

Contact Information for Business Card

TKV VENTURES NZ LTD
www.tkvventuresnz.co.nz

Howard Pennick
Phone +64 21 843 192
Email hdpennick@fernmail.co.nz

Font styles to use
Serif
Sans Serif

Colors
0792cd
33a6d7
85cae6
6b449b
886aae
f04a50
ec1f27
f37122
f68d4d

Requirements
Must have
• Please try and make the logo more modern or if you have a similar one we would like to see it.

```html
<!DOCTYPE html>
<html lang="en">
<head>
<meta charset="utf-8">
<title>TKV Ventures NZ LTD – Business Card</title>
<link rel="stylesheet" href="https://fonts.googleapis.com/css2?family=Cinzel:wght@500;600&family=Roboto:wght@400&display=swap">
<style>
  :root {
    --canvas-bg: #e9e7e5;
    --card-black: #151515;
    --text-white: #f2f2f2;
    --text-soft: #d9d9d9;
    --accent-orange: #f37122;
    --accent-purple: #6b449b;
    --accent-red: #ec1f27;
    --silver: #bdbdbd;
    --divider: #8a8a8a;
  }
  * { margin: 0; padding: 0; box-sizing: border-box; }
  html, body {
    width: 1200px; height: 780px; overflow: hidden;
    background: var(--canvas-bg);
  }
  .canvas {
    width: 1200px; height: 780px;
    display: flex; align-items: center; justify-content: center; gap: 40px;
  }
  .card {
    position: relative;
    width: 540px; height: 310px;
    background: var(--card-black);
    border-radius: 16px;
    overflow: hidden;
    box-shadow: 0 10px 30px rgba(0,0,0,0.25);
  }

  /* Front */
  .front-brand {
    position: absolute; left: 40px; top: 120px; width: 190px;
    display: flex; align-items: center; gap: 10px;
  }
  .brand-square {
    width: 22px; height: 22px; background: var(--accent-purple); flex: none;
  }
  .brand-name {
    font-family: 'Roboto', sans-serif; font-weight: 400;
    font-size: 15px; color: var(--text-white); line-height: 1.25;
  }
  .divider {
    position: absolute; left: 250px; top: 92px;
    width: 1px; height: 118px; background: var(--divider);
  }
  .contact-block { position: absolute; left: 272px; top: 90px; }
  .person-name {
    font-family: 'Cinzel', serif; font-weight: 600;
    font-size: 17px; letter-spacing: 0.5px; color: var(--text-white);
  }
  .person-title {
    font-family: 'Roboto', sans-serif; font-size: 13px;
    color: var(--accent-orange); margin-top: 2px;
  }
  .contact-list { list-style: none; margin-top: 10px; }
  .contact-list li {
    display: flex; align-items: center; gap: 9px;
    font-family: 'Roboto', sans-serif; font-size: 13px;
    color: var(--text-soft); height: 21px;
  }
  .contact-list svg { width: 12px; height: 12px; flex: none; }
  .stripe {
    position: absolute; left: 0; right: 0; bottom: 26px; height: 4px;
    display: flex;
  }
  .stripe-purple { width: 44%; background: var(--accent-purple); }
  .stripe-red { flex: 1; background: var(--accent-red); }

  /* Back */
  .back-brand {
    position: absolute; inset: 0;
    display: flex; flex-direction: column; align-items: center; justify-content: center;
  }
  .back-square {
    width: 40px; height: 40px; background: var(--silver); margin-bottom: 22px;
  }
  .company-name {
    font-family: 'Cinzel', serif; font-weight: 500;
    font-size: 22px; letter-spacing: 1px; color: var(--silver);
  }
  .company-tagline {
    font-family: 'Roboto', sans-serif; font-size: 9.5px;
    letter-spacing: 2.2px; color: var(--silver); margin-top: 4px;
  }
</style>
</head>
<body>
<main class="canvas">

  <section class="card card-front">
    <div class="front-brand">
      <span class="brand-square"></span>
      <span class="brand-name">TKV Ventures NZ LTD</span>
    </div>
    <div class="divider"></div>
    <div class="contact-block">
      <h1 class="person-name">HOWARD PENNICK</h1>
      <p class="person-title">Managing Director</p>
      <ul class="contact-list">
        <li>
          <svg viewBox="0 0 12 12" aria-hidden="true"><path fill="#f37122" d="M1 3.5 C1 2 2 1 3.5 1 L8.5 1 C10 1 11 2 11 3.5 L11 4.5 L8.5 4.5 L8.5 3.5 L3.5 3.5 L3.5 4.5 L1 4.5 Z M2 6 L10 6 L11 11 L1 11 Z"/></svg>
          +64 21 843 192
        </li>
        <li>
          <svg viewBox="0 0 12 12" aria-hidden="true"><rect x="0.5" y="2" width="11" height="8" fill="#f37122"/><path d="M0.5 2 L6 6.5 L11.5 2" fill="none" stroke="#151515" stroke-width="1"/></svg>
          hdpennick@fernmail.co.nz
        </li>
        <li>
          <svg viewBox="0 0 12 12" aria-hidden="true"><circle cx="6" cy="6" r="5.5" fill="#f37122"/><path d="M0.5 6 H11.5 M6 0.5 V11.5 M6 0.5 C3 3 3 9 6 11.5 M6 0.5 C9 3 9 9 6 11.5" fill="none" stroke="#151515" stroke-width="0.7"/></svg>
          www.tkvventuresnz.co.nz
        </li>
      </ul>
    </div>
    <div class="stripe"><span class="stripe-purple"></span><span class="stripe-red"></span></div>
  </section>

  <section class="card card-back">
    <div class="back-brand">
      <span class="back-square"></span>
      <h2 class="company-name">TKV VENTURES NZ LTD</h2>
      <p class="company-tagline">HOUSING AND COMMERCIAL BUILDINGS</p>
    </div>
  </section>

</main>
</body>
</html>
```